photowall advertisement

We require a wall featuring our company logo. We would like to avoid the color green, and gold is highly preferred. The design should be similar to the one in the attached photo. The wall will be used for photos and promotional purposes during congresses. Files must be prepared for printing.
dimension of wall: 470x223 cm

Industry/Entity Type

lifestyle

Colors
0054AA
0677BA
7BADD7
CADEEF
E8F1F8
6B429C
8869AF
B7A5CE
E3DAEB
F3F0F8

Requirements
Must have
• gold color, white, and other compare with gold color
Nice to have
• some pictograms, maps of Europe

```html
<!DOCTYPE html>
<html lang="en">
<head>
<meta charset="utf-8">
<title>Zorvalen Dynamics Photowall</title>
<link rel="stylesheet" href="https://fonts.googleapis.com/css2?family=Michroma&display=swap">
<style>
  :root {
    --page-bg: #44423a;
    --wall-white: #ffffff;
    --wall-gold: #ebdfcc;
    --map-gold: #d9bf92;
    --ink: #111111;
    --cell-w: 87.56px;
    --cell-h: 62.33px;
  }
  * { margin: 0; padding: 0; box-sizing: border-box; }
  html, body {
    width: 968px; height: 1200px; overflow: hidden;
    background: var(--page-bg);
  }
  .photowall {
    position: absolute; left: 90px; top: 728px;
    width: 788px; height: 374px;
    background: var(--wall-white);
    overflow: hidden;
    box-shadow: 0 6px 18px rgba(0,0,0,0.35);
    font-family: "Michroma", sans-serif;
    color: var(--ink);
  }
  .tile-grid {
    position: absolute; inset: 0;
    display: grid;
    grid-template-columns: repeat(9, 1fr);
    grid-template-rows: repeat(6, 1fr);
  }
  .tile { background: var(--wall-white); }
  .tile--gold { background: var(--wall-gold); }
  .europe-map {
    position: absolute; left: 150px; top: 20px;
    width: 480px; height: 354px;
    background: radial-gradient(ellipse at 50% 50%, rgba(217,191,146,0.35) 0%, rgba(217,191,146,0.15) 45%, rgba(217,191,146,0) 72%);
  }
  .brand {
    position: absolute;
    display: flex; flex-direction: column; align-items: center; justify-content: center;
    white-space: nowrap;
    height: var(--cell-h);
    line-height: 1;
  }
  .brand--name { width: calc(var(--cell-w) * 2); }
  .brand__name { font-size: 14px; letter-spacing: 0.02em; }
  .brand__sub { font-size: 6.5px; letter-spacing: 0.42em; margin-top: 4px; padding-left: 0.42em; }
  .brand--short { width: var(--cell-w); font-size: 30px; }
  .brand-hero {
    position: absolute; left: calc(var(--cell-w) * 2); top: calc(var(--cell-h) * 2);
    width: calc(var(--cell-w) * 5); height: calc(var(--cell-h) * 2);
    display: flex; align-items: center; justify-content: center; gap: 20px;
    white-space: nowrap; line-height: 1;
  }
  .brand-hero__short { font-size: 58px; }
  .brand-hero__text { display: flex; flex-direction: column; align-items: center; }
  .brand-hero__name { font-size: 25px; letter-spacing: 0.02em; }
  .brand-hero__sub { font-size: 11px; letter-spacing: 0.42em; margin-top: 7px; padding-left: 0.42em; }
</style>
</head>
<body>
<main class="photowall">
  <div class="tile-grid">
    <div class="tile tile--gold"></div><div class="tile"></div><div class="tile tile--gold"></div><div class="tile"></div><div class="tile tile--gold"></div><div class="tile"></div><div class="tile tile--gold"></div><div class="tile"></div><div class="tile tile--gold"></div>
    <div class="tile"></div><div class="tile tile--gold"></div><div class="tile"></div><div class="tile tile--gold"></div><div class="tile"></div><div class="tile tile--gold"></div><div class="tile"></div><div class="tile tile--gold"></div><div class="tile"></div>
    <div class="tile tile--gold"></div><div class="tile"></div><div class="tile"></div><div class="tile"></div><div class="tile"></div><div class="tile"></div><div class="tile"></div><div class="tile"></div><div class="tile tile--gold"></div>
    <div class="tile"></div><div class="tile tile--gold"></div><div class="tile"></div><div class="tile"></div><div class="tile"></div><div class="tile"></div><div class="tile"></div><div class="tile tile--gold"></div><div class="tile"></div>
    <div class="tile tile--gold"></div><div class="tile"></div><div class="tile tile--gold"></div><div class="tile"></div><div class="tile tile--gold"></div><div class="tile"></div><div class="tile tile--gold"></div><div class="tile"></div><div class="tile tile--gold"></div>
    <div class="tile"></div><div class="tile tile--gold"></div><div class="tile"></div><div class="tile tile--gold"></div><div class="tile"></div><div class="tile tile--gold"></div><div class="tile"></div><div class="tile tile--gold"></div><div class="tile"></div>
  </div>

  <div class="europe-map" role="img" aria-label="Dotted gold map of Europe"></div>

  <div class="brand brand--short" style="left:0;top:0">ZD</div>
  <div class="brand brand--name" style="left:calc(var(--cell-w)*2);top:0"><span class="brand__name">ZORVALEN</span><span class="brand__sub">DYNAMICS</span></div>
  <div class="brand brand--short" style="left:calc(var(--cell-w)*5);top:0">ZD</div>
  <div class="brand brand--name" style="left:calc(var(--cell-w)*7);top:0"><span class="brand__name">ZORVALEN</span><span class="brand__sub">DYNAMICS</span></div>

  <div class="brand brand--name" style="left:0;top:var(--cell-h)"><span class="brand__name">ZORVALEN</span><span class="brand__sub">DYNAMICS</span></div>
  <div class="brand brand--short" style="left:calc(var(--cell-w)*3);top:var(--cell-h)">ZD</div>
  <div class="brand brand--name" style="left:calc(var(--cell-w)*5);top:var(--cell-h)"><span class="brand__name">ZORVALEN</span><span class="brand__sub">DYNAMICS</span></div>

  <div class="brand brand--short" style="left:var(--cell-w);top:calc(var(--cell-h)*2)">ZD</div>
  <div class="brand brand--short" style="left:calc(var(--cell-w)*7);top:calc(var(--cell-h)*2)">ZD</div>

  <div class="brand brand--name" style="left:0;top:calc(var(--cell-h)*3)"><span class="brand__name">ZORVALEN</span><span class="brand__sub">DYNAMICS</span></div>

  <div class="brand brand--short" style="left:0;top:calc(var(--cell-h)*4)">ZD</div>
  <div class="brand brand--short" style="left:calc(var(--cell-w)*3);top:calc(var(--cell-h)*4)">ZD</div>
  <div class="brand brand--short" style="left:calc(var(--cell-w)*6);top:calc(var(--cell-h)*4)">ZD</div>
  <div class="brand brand--name" style="left:calc(var(--cell-w)*7);top:calc(var(--cell-h)*4)"><span class="brand__name">ZORVALEN</span><span class="brand__sub">DYNAMICS</span></div>

  <div class="brand brand--name" style="left:var(--cell-w);top:calc(var(--cell-h)*5)"><span class="brand__name">ZORVALEN</span><span class="brand__sub">DYNAMICS</span></div>
  <div class="brand brand--name" style="left:calc(var(--cell-w)*4);top:calc(var(--cell-h)*5)"><span class="brand__name">ZORVALEN</span><span class="brand__sub">DYNAMICS</span></div>
  <div class="brand brand--short" style="left:calc(var(--cell-w)*8);top:calc(var(--cell-h)*5)">ZD</div>

  <div class="brand-hero">
    <span class="brand-hero__short">ZD</span>
    <span class="brand-hero__text">
      <span class="brand-hero__name">ZORVALEN</span>
      <span class="brand-hero__sub">DYNAMICS</span>
    </span>
  </div>
</main>
</body>
</html>
```